A5 Patient Information Booklet (Chiropractic Clinic) 4-8 pages

Here’s a polished, professional rewrite of your full brief and content, with clearer structure, corrected language, and a premium tone:

---

**Project Title:** Premium Patient Information Brochure (Chiropractic & Wellness Clinic)

---

### **Overview**

We are a health and wellness clinic seeking a premium, high-end patient information brochure to provide following a patient’s initial consultation and first treatment.

The purpose of this booklet is to:

* Reinforce trust and professionalism
* Help patients understand what to expect next
* Encourage adherence to care recommendations
* Position the clinic as calm, expert-led, and results-driven

---

### **Format**

* 4–8 page booklet (A5 or similar size)
* Print-ready and digital versions required

---

### **Target Audience**

Patients who have just completed their initial consultation and may have begun treatment. They may already be experiencing physical or mental changes, so the brochure should guide, reassure, and educate them on what comes next.

---

### **Tone & Style**

* Premium, calm, and reassuring
* Modern wellness aesthetic (not overly clinical)
* Clean layout with minimal clutter
* Soft, neutral colour palette (whites, creams, muted greens, soft blues)
* Elegant typography (e.g. Montserrat / Lato)
* High-end, trustworthy, and professional feel

---

### **Key Messages**

#### 1. Listen to Your Body

Patients may feel different after treatment. Reassure them that this is normal and part of the healing process.

#### 2. Post-Treatment Advice

* Stay well hydrated
* Rest if needed
* Avoid overexertion if the body requires recovery

#### 3. Healing is a Journey (Core Concept)

A strong visual metaphor of a **“road to recovery”** or **journey** should be central to the design.

This journey should clearly illustrate three phases:

* **Phase 1: Initial Care (Weeks 1–6)**
Focus: Reducing pain/discomfort, calming the body, and initiating response to treatment

* **Phase 2: Corrective Care (Weeks 6–12)**
Focus: Addressing underlying issues, improving function, and creating lasting change

* **Phase 3: Wellness / Maintenance (Ongoing)**
Focus: Maintaining progress, preventing relapse, and supporting long-term wellbeing

**Important:**

* Emphasise that this is not a quick fix
* Progress requires time and consistency
* Each patient follows an individualised care plan
* The journey should feel structured, positive, and achievable

#### 4. Personalised Care

Reinforce that every treatment plan is tailored specifically to the individual.

#### 5. Professional Reassurance

Patients should feel confident they are in expert hands and supported throughout their journey.

---

### **Design Direction**

* Use imagery that reflects calmness, progression, and wellness (e.g. pathways, nature, soft gradients)
* Avoid generic stock imagery
* **Only use original clinic images from website and social media**
* Prioritise white space and clarity
* Aim for a luxury spa/medical hybrid aesthetic

---

## **Content Structure (Page-by-Page)**

### **Front Cover**

* Clean, minimal, premium design
* Clinic branding

---

### **Page 1: Patient Case Summary**

**Title:** *Welcome to Fernwell Practice*

Thank you for choosing Fernwell Practice.

This booklet is designed to guide you through:

* What we found during your initial consultation
* Your personalised recommended treatment plan
* Your road to recovery
* Long-term wellness care
* Why we take the approach we do

---

### **Page 2: Your Care Journey**

**Stage 1: Your Initial Consultation**

Today we completed a comprehensive assessment of your health and function, including:

* Full case history and discussion of your symptoms and goals
* Orthopaedic and neurological testing
* Postural and movement assessment
* Initial treatment (where appropriate)

**What this tells us:**

* How your body is currently functioning
* Where areas of stress or dysfunction may be present
* The most appropriate and effective path forward for your care

---

### **Page 3: Your Suggested Treatment Plan**

Based on today’s findings, your recommended care plan is:

**______ treatments over ______ weeks**

This should be viewed alongside your *Road to Recovery* to help you understand what to expect.

We have also discussed:

* Expected timelines for improvement
* Available payment options

**After Treatment:**
It is common to feel different following treatment. This is a normal response as your body begins to adapt and respond.

We recommend:

* Staying well hydrated
* Allowing time for rest and recovery
* Avoiding overexertion if your body feels it needs it

---

### **Page 4: What to Expect Next**

Healing is not always linear—it is a process that occurs over time.

Your care will typically progress through the following stages:

* **Relief Care**
Focused on reducing discomfort and calming the body

* **Corrective Care**
Focused on addressing underlying issues and improving function
(This phase may include prescribed exercises)

* **Maintenance / Wellness Care**
Focused on sustaining progress, preventing recurrence, and supporting long-term health

---

### **Page 5: Understanding Chiropractic Care**

**What is Chiropractic?**
Chiropractic care focuses on the relationship between the spine, nervous system, and overall body function.

By improving spinal movement and alignment, chiropractic care helps support the nervous system, allowing the body to function and heal more effectively.

**About Fernwell Practice**
At Fernwell Practice, our approach is centred around personalised, patient-focused care. We aim to not only relieve symptoms but to address underlying causes and support long-term wellbeing.

---

### **Back Page**

* Clinic contact details
* Website
* Social media icons/handles

**Closing Message:**
“A healthier, stronger you—supported every step of the way.”

---

### **Deliverables**

* Print-ready PDF
* Editable source files

---

### **Additional Notes**

* The brochure should feel valuable and worth keeping
* Encourage long-term care in a subtle, non-pushy way
* Maintain clarity, readability, and strong visual hierarchy
* Balance professionalism with warmth and approachability

---

If you’d like, I can also turn this into **actual brochure copy (fully written, patient-facing text)** or help you refine it further for a designer.

Target Market(s)

Existing patients who want to feel better and look after themselves that is given after their initil consultation appointment

Industry/Entity Type

Chiropractic, wellness, health

Font styles to use
Other font styles liked:
• Montserrat or Lato

Colors
0094D4
00A9DD
6FCCEA
C7EBF8
E9F6FB
00AB8E
00BBA5
67D7C9
C6EFE9
E9F9F6
6B429C
8869AF
B7A5CE
E3DAEB
F3F0F8

Requirements
Must have
• my own photos, look premium wellness, be clear and simple to understand for patients journey or what to expect next and over time
Nice to have
• USe my social media/website for ideas
Should not have
• generic photos and images

```html
<!DOCTYPE html>
<html lang="en">
<head>
<meta charset="utf-8">
<title>Fernwell Practice – Patient Booklet Pages</title>
<link href="https://fonts.googleapis.com/css2?family=Montserrat:wght@400;500;600;700;800&display=swap" rel="stylesheet">
<style>
  :root{
    --canvas:#ececec;
    --paper:#f9efe7;
    --ink:#1d1d1f;
    --muted:#4a4a4a;
    --teal:#19a89a;
    --teal-dark:#10968a;
    --pink:#ee86b8;
    --blue:#7fa6dc;
    --purple:#b48fd0;
    --white:#ffffff;
  }
  *{box-sizing:border-box;margin:0;padding:0}
  html,body{width:862px;height:1200px;overflow:hidden}
  body{background:var(--canvas);font-family:"Montserrat",sans-serif;color:var(--ink);position:relative}
  .page{position:absolute;width:256px;height:363px;background:var(--paper);overflow:hidden;box-shadow:0 6px 18px rgba(0,0,0,.16)}
  .page svg.art{position:absolute;inset:0;width:256px;height:363px}
  .abs{position:absolute}
  .center{left:0;right:0;text-align:center}

  /* brand name */
  .brand-name{font-weight:600;color:var(--ink);letter-spacing:.5px;text-transform:uppercase}
  .tagline{color:var(--teal);letter-spacing:1.6px;text-transform:uppercase;font-weight:500}

  /* cover */
  .cover .brand-name{top:127px;font-size:17px}
  .cover .tagline{top:150px;font-size:7.5px}
  .cover .site{top:340px;font-size:7.5px;color:var(--white)}

  /* expect page */
  .expect h2{left:17px;top:136px;font-size:15.5px;font-weight:700;line-height:20px}
  .expect h2 span{color:var(--teal);display:block}
  .expect h3{font-size:9.5px;font-weight:600}
  .expect .listen{left:17px;top:187px}
  .expect .note{left:17px;top:206px;width:200px;font-size:6.2px;line-height:8px;color:var(--muted)}
  .expect .advice-title{left:17px;top:242px}
  .advice-list{left:15px;top:258px;list-style:none}
  .advice-list li{display:flex;align-items:flex-start;gap:7px;font-size:7.5px;font-weight:600;height:25px}
  .advice-list small{display:block;font-size:4.6px;font-weight:400;color:var(--muted);margin-top:2px}
  .advice-list svg{width:13px;height:13px;flex:none}

  /* journey page */
  .journey h2{left:0;right:0;top:20px;text-align:center;font-size:13px;font-weight:700}
  .journey h2 span{color:var(--teal)}
  .phase{position:absolute;left:31px;width:194px;height:51px;border-radius:8px;color:var(--white);display:flex;align-items:center}
  .phase.teal{background:var(--teal)}
  .phase.pink{background:var(--pink);flex-direction:row-reverse}
  .phase-num{width:33px;height:45px;margin:0 3px;border:2px solid var(--white);border-radius:6px;background:var(--white);position:relative;flex:none}
  .phase.teal .phase-num{color:var(--teal)}
  .phase.pink .phase-num{color:var(--pink)}
  .phase-num i{position:absolute;top:3px;left:0;right:0;text-align:center;font-style:normal;font-size:3.5px;font-weight:700;letter-spacing:.3px}
  .phase-num b{position:absolute;top:7px;left:0;right:0;text-align:center;font-size:30px;line-height:34px;font-weight:800}
  .phase-text{padding:0 6px;flex:1}
  .phase-text h4{font-size:8.5px;font-weight:600;margin-bottom:3px}
  .phase-text p{font-size:5.2px;line-height:6.2px}
  .phase-text p strong{font-weight:700}
  .journey .important{left:33px;top:250px;width:200px}
  .important h4{font-size:7.5px;font-weight:700;margin-bottom:2px}
  .important ul{list-style:none;font-size:4.6px;line-height:6.3px}
  .important li::before{content:"• "}
  .journey .point{left:33px;width:196px}
  .point h4{font-size:7.5px;font-weight:700}
  .point p{font-size:4.6px;line-height:5.6px;color:var(--muted)}

  /* personalisation page */
  .personal .brand-name{top:70px;font-size:7px}
  .personal .tagline{top:80px;font-size:3.4px;letter-spacing:.8px}
  .form-card{left:17px;top:89px;width:222px;height:92px;border:1.5px solid var(--pink);border-radius:6px;background:var(--paper);padding:8px 10px}
  .form-card h2{font-size:12.5px;font-weight:700;text-align:center;margin-bottom:8px}
  .field{font-size:5px;font-weight:600;display:flex;align-items:flex-end;gap:2px;margin-bottom:10px}
  .field .line{flex:1;border-bottom:.6px solid var(--ink);height:5px}
  .field .short{flex:none;width:46px}

  /* back page */
  .back .brand-name{top:204px;font-size:16px}
  .back .tagline{top:226px;font-size:7px}
  .back .handle{left:18px;top:333px;width:90px;text-align:center;font-size:5px;font-weight:600}
  .back .contact{left:138px;top:326px;font-size:4.6px;font-weight:600;line-height:7px}
  .social{left:52px;top:318px;display:flex;gap:3px}
  .social span{width:9px;height:9px;border-radius:50%;background:var(--ink);display:block}
</style>
</head>
<body>

<!-- shared gradients -->
<svg width="0" height="0" style="position:absolute">
  <defs>
    <linearGradient id="arcGrad" x1="0" y1="0" x2="1" y2="0">
      <stop offset="0" stop-color="#7fa6dc"/>
      <stop offset=".5" stop-color="#b48fd0"/>
      <stop offset="1" stop-color="#ea8bbf"/>
    </linearGradient>
    <linearGradient id="ringGrad" x1="0" y1="0" x2="1" y2="1">
      <stop offset="0" stop-color="#ee86b8"/>
      <stop offset="1" stop-color="#7fa6dc"/>
    </linearGradient>
    <linearGradient id="monoPhoto" x1="0" y1="0" x2="1" y2="1">
      <stop offset="0" stop-color="#cfcfcf"/>
      <stop offset=".55" stop-color="#6e6e6e"/>
      <stop offset="1" stop-color="#262626"/>
    </linearGradient>
    <linearGradient id="warmPhoto" x1="0" y1="0" x2="1" y2="1">
      <stop offset="0" stop-color="#d9c8b8"/>
      <stop offset=".5" stop-color="#efe9e4"/>
      <stop offset="1" stop-color="#b89a7e"/>
    </linearGradient>
    <linearGradient id="paperPhoto" x1="0" y1="0" x2="1" y2="1">
      <stop offset="0" stop-color="#f2f2f0"/>
      <stop offset=".7" stop-color="#e2e2e0"/>
      <stop offset="1" stop-color="#a8835c"/>
    </linearGradient>
  </defs>
</svg>

<!-- Cover -->
<section class="page cover" style="left:25px;top:220px">
  <svg class="art" viewBox="0 0 256 363">
    <circle cx="128" cy="74" r="45" fill="none" stroke="url(#ringGrad)" stroke-width="2.5"/>
    <path d="M40 230 Q128 160 216 230 Q128 178 40 230Z" fill="url(#arcGrad)"/>
    <circle cx="128" cy="332" r="132" fill="url(#monoPhoto)" role="img" aria-label="Black and white photo of the chiropractor treating a patient's back"/>
  </svg>
  <div class="abs center brand-name">Fernwell Practice</div>
  <div class="abs center tagline">Chiropractic &amp; Wellness</div>
  <div class="abs center site">www.fernwellpractice.co.uk</div>
</section>

<!-- What to expect -->
<section class="page expect" style="left:303px;top:220px">
  <svg class="art" viewBox="0 0 256 363">
    <circle cx="128" cy="-22" r="122" fill="url(#warmPhoto)" role="img" aria-label="Photo of a patient lying face down receiving hands-on back treatment"/>
    <path d="M36 110 Q128 172 220 110 Q128 154 36 110Z" fill="url(#arcGrad)"/>
    <path d="M0 234 H192 A56 56 0 0 1 192 346 H0" fill="none" stroke="url(#arcGrad)" stroke-width="1.2"/>
    <circle cx="198" cy="290" r="42" fill="none" stroke="url(#ringGrad)" stroke-width="2.5"/>
  </svg>
  <h2 class="abs">What to expect after<span>your treatment</span></h2>
  <h3 class="abs listen">1. Listen to Your Body</h3>
  <p class="abs note">Patients may feel different after treatment. Encourage awareness and reassurance that this is normal.</p>
  <h3 class="abs advice-title">2. Post-Treatment Advice</h3>
  <ul class="abs advice-list">
    <li><svg viewBox="0 0 14 14"><path d="M3 2h8l-1 10H4Z" fill="none" stroke="#19a89a" stroke-width="1"/><path d="M7 6c-1 1.4-1.4 2-1.4 2.6a1.4 1.4 0 0 0 2.8 0C8.4 8 8 7.4 7 6Z" fill="#19a89a"/></svg>Stay well hydrated</li>
    <li><svg viewBox="0 0 14 14"><rect x="2" y="5" width="10" height="6" rx="1" fill="none" stroke="#ee86b8" stroke-width="1"/><path d="M2 11v2M12 11v2M4 5V3h6v2" fill="none" stroke="#ee86b8" stroke-width="1"/></svg>Rest if needed</li>
    <li><svg viewBox="0 0 14 14"><circle cx="7" cy="4" r="2" fill="none" stroke="#19a89a" stroke-width="1"/><path d="M3 13v-3a4 3 0 0 1 8 0v3" fill="none" stroke="#19a89a" stroke-width="1"/></svg><div>Avoid overexertion<small>if the body feels like it needs recovery</small></div></li>
  </ul>
</section>

<!-- Recovery journey -->
<section class="page journey" style="left:581px;top:220px">
  <svg class="art" viewBox="0 0 256 363">
    <path d="M47 100v6h170v13M47 170v6h170v10" fill="none" stroke="#1d1d1f" stroke-width=".6" stroke-dasharray="1.5 1.5"/>
  </svg>
  <h2 class="abs">YOUR RECOVERY <span>JOURNEY</span></h2>
  <div class="phase teal" style="top:49px">
    <div class="phase-num"><i>PHASE</i><b>1</b></div>
    <div class="phase-text"><h4>Initial Care (Weeks 1–6)</h4><p><strong>Focus:</strong> Reducing pain/discomfort, calming the body, and helping you begin to respond to treatment.</p></div>
  </div>
  <div class="phase pink" style="top:119px">
    <div class="phase-num"><i>PHASE</i><b>2</b></div>
    <div class="phase-text"><h4>Initial Care (Weeks 1–6)</h4><p><strong>Focus:</strong> Reducing pain/discomfort, calming the body, and helping you begin to respond to treatment.</p></div>
  </div>
  <div class="phase teal" style="top:186px">
    <div class="phase-num"><i>PHASE</i><b>3</b></div>
    <div class="phase-text"><h4>Initial Care (Weeks 1–6)</h4><p><strong>Focus:</strong> Reducing pain/discomfort, calming the body, and helping you begin to respond to treatment.</p></div>
  </div>
  <div class="abs important">
    <h4>Important:</h4>
    <ul>
      <li>This visual should clearly communicate that this is not <strong>a quick fix</strong></li>
      <li>Progress takes time and consistency</li>
      <li>Each patient will follow an <strong>individualised treatment plan</strong></li>
      <li>The journey should feel positive, structured, and achievable</li>
    </ul>
  </div>
  <div class="abs point" style="top:298px"><h4>4. Personalised Care</h4><p>Reinforce that each patient's treatment plan is tailored specifically to them.</p></div>
  <div class="abs point" style="top:326px"><h4>5. Professional Reassurance</h4><p>Patients should feel confident they are in expert hands and supported throughout their journey.</p></div>
</section>

<!-- Personalisation -->
<section class="page personal" style="left:164px;top:614px">
  <svg class="art" viewBox="0 0 256 363">
    <circle cx="128" cy="37" r="20" fill="none" stroke="url(#ringGrad)" stroke-width="1.6"/>
    <path d="M38 240 Q128 170 218 240 Q128 188 38 240Z" fill="url(#arcGrad)"/>
    <circle cx="128" cy="350" r="144" fill="url(#paperPhoto)" role="img" aria-label="Photo of an anatomical spine chart on paper"/>
  </svg>
  <div class="abs center brand-name">Fernwell Practice</div>
  <div class="abs center tagline">Chiropractic &amp; Wellness</div>
  <div class="abs form-card">
    <h2>PERSONALISATION SECTION</h2>
    <div class="field">Patient Name: <span class="line"></span></div>
    <div class="field">Your Suggested Care Plan:</div>
    <div class="field"><span class="line"></span></div>
    <div class="field">treatments over <span class="line short"></span> weeks.</div>
  </div>
</section>

<!-- Back page -->
<section class="page back" style="left:442px;top:614px">
  <svg class="art" viewBox="0 0 256 363">
    <circle cx="128" cy="232" r="110" fill="none" stroke="#f1dfe6" stroke-width="10" opacity=".5"/>
    <circle cx="128" cy="151" r="43" fill="none" stroke="url(#ringGrad)" stroke-width="2.5"/>
  </svg>
  <div class="abs center brand-name">Fernwell Practice</div>
  <div class="abs center tagline">Chiropractic &amp; Wellness</div>
  <div class="abs social"><span></span><span></span></div>
  <div class="abs handle">fernwell_practice</div>
  <div class="abs contact">www.fernwellpractice.co.uk<br>12 Mill Lane, Ashbury AB1 2CD</div>
</section>

</body>
</html>
```